Harbor Card Design

IT consulting services - my company focuses on delivering value add for clients through sourcing services, strategic and project consulting services, as well as delivering office fitout project managment services.
We also offer IT Interim managment services - to fill the gap when looking for executive roles.
I use orange and blue as my corporate colours
I am after a simple design with my details on the front and my services not the back
Industry/Entity Type
It Company
Contact Information for Business Card
Owen Tredwick
Director
Brightwell Solutions
Owen.Tredwick@BrightwellSolutions.example.au
www.BrightwellSolutions.example.au
m: +61 400582617
On Rear of card:
Interim Management
Project and Strategy Consulting
Sourcing Services
Commercial fit-out management

```html
<!DOCTYPE html>
<html lang="en">
<head>
<meta charset="utf-8">
<title>Brightwell Solutions – Business Card</title>
<link rel="stylesheet" href="https://fonts.googleapis.com/css2?family=Cinzel:wght@400;500&family=Open+Sans:wght@600&display=swap">
<style>
  :root {
    --page: #e9e7e4;
    --card-white: #f7f7f7;
    --brand-orange: #fba00f;
    --brand-blue: #163a73;
    --text-light: #ffffff;
  }
  * { box-sizing: border-box; margin: 0; padding: 0; }
  html, body { width: 1200px; height: 899px; overflow: hidden; }
  body { background: var(--page); position: relative; }

  .card {
    position: absolute;
    left: 180px; top: 210px;
    width: 840px; height: 480px;
    border-radius: 40px;
    overflow: hidden;
    background: var(--card-white);
    box-shadow: 0 10px 30px rgba(0,0,0,0.15);
  }
  .card-shapes { position: absolute; inset: 0; }

  .brand {
    position: absolute;
    left: 30px; top: 210px;
    display: flex; align-items: center; gap: 9px;
  }
  .brand-square {
    width: 20px; height: 20px;
    background: var(--brand-orange);
    flex: none;
  }
  .brand-name {
    font-family: "Open Sans", sans-serif;
    font-weight: 600;
    font-size: 24px;
    color: var(--brand-blue);
    white-space: nowrap;
  }

  .identity {
    position: absolute;
    left: 470px; top: 78px;
    color: var(--text-light);
    font-family: "Cinzel", serif;
  }
  .person-name { font-size: 30px; font-weight: 400; letter-spacing: 1.5px; }
  .person-title { font-size: 20px; letter-spacing: 1px; margin-top: 4px; }

  .contact-list {
    position: absolute;
    left: 420px; top: 300px;
    list-style: none;
    color: var(--text-light);
    font-family: "Cinzel", serif;
    font-size: 13px;
    line-height: 24px;
    white-space: nowrap;
  }
  .contact-list li { display: flex; align-items: center; gap: 9px; }
  .contact-icon { width: 13px; height: 13px; flex: none; }
</style>
</head>
<body>
  <div class="card">
    <svg class="card-shapes" viewBox="0 0 840 480" width="840" height="480" aria-hidden="true">
      <path d="M392 0 Q362 260 300 480 L840 480 L840 0 Z" fill="var(--brand-orange)"/>
      <path d="M352 0 Q334 260 283 480 L300 480 Q362 260 392 0 Z" fill="var(--brand-blue)"/>
    </svg>

    <div class="brand">
      <span class="brand-square"></span>
      <span class="brand-name">Brightwell Solutions</span>
    </div>

    <div class="identity">
      <p class="person-name">Owen Tredwick</p>
      <p class="person-title">Director</p>
    </div>

    <ul class="contact-list">
      <li>
        <svg class="contact-icon" viewBox="0 0 14 14"><circle cx="7" cy="7" r="7" fill="#fff"/><rect x="4.6" y="3" width="4.8" height="8" rx="1" fill="var(--brand-orange)"/></svg>
        <span>m: +61 400582617</span>
      </li>
      <li>
        <svg class="contact-icon" viewBox="0 0 14 14"><circle cx="7" cy="7" r="7" fill="#fff"/><rect x="3.3" y="4.3" width="7.4" height="5.4" fill="var(--brand-orange)"/><path d="M3.3 4.3L7 7.3l3.7-3" stroke="#fff" stroke-width="0.8" fill="none"/></svg>
        <span>Owen.Tredwick@BrightwellSolutions.example.au</span>
      </li>
      <li>
        <svg class="contact-icon" viewBox="0 0 14 14"><circle cx="7" cy="7" r="7" fill="#fff"/><circle cx="7" cy="7" r="3.6" stroke="var(--brand-orange)" stroke-width="1" fill="none"/><path d="M3.4 7h7.2M7 3.4v7.2" stroke="var(--brand-orange)" stroke-width="0.8"/></svg>
        <span>www.BrightwellSolutions.example.au</span>
      </li>
    </ul>
  </div>
</body>
</html>
```